Financial Services Flyer for Healthcare Providers

We need a flyer design for a product of Talvo Financial (www.talvofinancial.example) called the PLUM program. Attached you will find the content for the flyer. Please use your own creativity and keep in mind the this is a product of Talvo Financial, a financial services company that works in the field of healthcare. If you have any questions or comments, please feel free to ask....

Target Market(s)

Our target audience is healthcare providers.

Industry/Entity Type

Financial

Requirements
Must have
• Eye catching graphics and colors but still look fairly conservative since our audience is somewhat conservative.
Nice to have
• Nice looking, smiling, upbeat people in pictorial portions of the flyer.
Should not have
• Our clients are all found in America, so the look, feel and subtext should all target an American audience and not have the look and feel of being from outside of the US.

```html
<!DOCTYPE html>
<html lang="en">
<head>
<meta charset="utf-8">
<title>PLUM Program Flyer – Talvo Financial</title>
<link rel="stylesheet" href="https://fonts.googleapis.com/css2?family=Titillium+Web:wght@400;600;700&family=Open+Sans:wght@400;600;700&display=swap">
<style>
  :root {
    --sky: #29a8e0;
    --ink: #222222;
    --slate: #6d6e71;
    --maroon: #6b1c1c;
    --paper: #ffffff;
    --backdrop: #e9e9e9;
    --photo-top: #eef2f5;
    --photo-bottom: #b9c3cc;
  }
  * { box-sizing: border-box; margin: 0; padding: 0; }
  html, body { width: 953px; height: 1200px; overflow: hidden; }
  body { background: var(--backdrop); font-family: "Open Sans", Arial, sans-serif; color: var(--ink); }

  .flyer { position: absolute; left: 51px; top: 50px; width: 850px; height: 1100px; background: var(--paper); overflow: hidden; box-shadow: 0 4px 16px rgba(0,0,0,.18); }

  .brand { position: absolute; left: 30px; top: 48px; display: flex; align-items: center; gap: 14px; }
  .brand-square { width: 40px; height: 40px; background: var(--slate); border-radius: 6px; }
  .brand-name { font-family: "Titillium Web", sans-serif; font-weight: 600; font-size: 40px; color: var(--ink); letter-spacing: .5px; line-height: 1; }
  .brand-divider { position: absolute; left: 366px; top: 42px; width: 1px; height: 68px; background: #bbb; }
  .tagline { position: absolute; left: 388px; top: 40px; font-size: 20px; line-height: 24px; letter-spacing: .5px; }
  .tagline .t1 { color: var(--maroon); }
  .tagline .t2 { color: #333; }
  .tagline .t3 { color: #888; }

  .hero { position: absolute; left: 0; top: 134px; width: 850px; height: 466px; background: linear-gradient(180deg, var(--photo-top) 0%, #dfe5ea 55%, var(--photo-bottom) 100%); }
  .hero-band { position: absolute; left: 0; top: 259px; width: 850px; height: 112px; background: rgba(120,160,200,.45); }
  .hero-title { position: absolute; left: 0; width: 850px; top: 287px; text-align: center; font-family: "Open Sans", sans-serif; font-weight: 700; font-size: 46px; color: #fff; letter-spacing: 1px; text-shadow: 0 1px 3px rgba(0,0,0,.25); }
  .hero-caption { position: absolute; left: 30px; top: 396px; width: 402px; height: 54px; background: #77787b; color: #fff; font-family: "Titillium Web", sans-serif; font-size: 20px; line-height: 54px; padding-left: 14px; }

  .section-title { font-family: "Titillium Web", sans-serif; font-weight: 600; color: var(--sky); font-size: 24px; line-height: 1; white-space: nowrap; }
  .body-copy { font-size: 15px; line-height: 22px; color: var(--ink); text-align: justify; }
  .accent { color: var(--sky); }

  .intro { position: absolute; left: 29px; top: 650px; width: 352px; }
  .intro .section-title { font-size: 23px; letter-spacing: -.2px; }
  .intro .body-copy { margin-top: 22px; padding-left: 4px; }
  .intro .body-copy + .body-copy { margin-top: 5px; }

  .costs { position: absolute; left: 29px; top: 905px; width: 352px; }
  .costs .body-copy { margin-top: 16px; padding-left: 4px; text-align: left; line-height: 25px; }

  .how { position: absolute; left: 473px; top: 630px; width: 377px; height: 381px; background: var(--sky); border-radius: 26px 0 0 26px; }
  .how .section-title { color: #fff; position: absolute; left: 28px; top: 20px; }
  .step { position: absolute; left: 48px; width: 310px; color: #fff; }
  .step h3 { font-family: "Titillium Web", sans-serif; font-weight: 600; font-size: 16px; line-height: 20px; }
  .step p { font-size: 11.5px; line-height: 14px; margin-top: 2px; }
  .step-icon { position: absolute; left: -72px; width: 58px; height: 58px; }

  .cta { position: absolute; left: 0; top: 1040px; width: 850px; height: 60px; background: var(--sky); color: #fff; font-family: "Titillium Web", sans-serif; font-weight: 700; font-size: 29px; }
  .cta-label { position: absolute; left: 138px; top: 10px; }
  .cta-icon { position: absolute; left: 406px; top: 11px; width: 38px; height: 38px; }
  .cta-phone { position: absolute; left: 470px; top: 10px; }
</style>
</head>
<body>
<main class="flyer">
  <div class="brand"><span class="brand-square"></span><span class="brand-name">Talvo Financial</span></div>
  <div class="brand-divider"></div>
  <div class="tagline"><div class="t1">Receivable</div><div class="t2">Management</div><div class="t3">Solutions</div></div>

  <section class="hero" role="img" aria-label="Smiling businessman in a grey suit standing with arms crossed in front of a bright office where headset-wearing billing staff work at computers">
    <div class="hero-band"></div>
    <h1 class="hero-title">PLUM Program</h1>
    <div class="hero-caption">PLUM Has recovered millions for Hospitals</div>
  </section>

  <section class="intro">
    <h2 class="section-title">Claims Evaluation &amp; Recovery Team</h2>
    <p class="body-copy">At Talvo financial, <span class="accent">PLUM</span> locates underpaid claims and turns write offs into added revenue.</p>
    <p class="body-copy"><span class="accent">PLUM</span> uses a genius revenue cycle application that identifies potentially underpaid claims for hospitals. Once revenue has been located, our medical billers correct the claims and appeal to insurance for payment.</p>
  </section>

  <section class="costs">
    <h2 class="section-title">Costs</h2>
    <p class="body-copy"><span class="accent">PLUM</span> charges nothing unless it finds and collects lost revenue for you!</p>
  </section>

  <section class="how">
    <h2 class="section-title">How PLUM works</h2>

    <div class="step" style="top:78px">
      <svg class="step-icon" style="top:-10px" viewBox="0 0 58 58" aria-hidden="true">
        <circle cx="29" cy="29" r="28" fill="#6d6e71" stroke="#fff" stroke-width="1"/>
        <path d="M19 29a10 10 0 0 1 17-7" fill="none" stroke="#fff" stroke-width="3.5"/>
        <path d="M39 29a10 10 0 0 1-17 7" fill="none" stroke="#fff" stroke-width="3.5"/>
        <path d="M33 17l6 4-6 4z" fill="#fff"/>
        <path d="M25 41l-6-4 6-4z" fill="#fff"/>
      </svg>
      <h3>Remote Evaluation:</h3>
      <p>With a secure and temporary login into any healthcare operating system a random account evaluation is conducted by a highly skilled revenue cycle auditor.</p>
    </div>

    <div class="step" style="top:179px">
      <svg class="step-icon" style="top:-10px" viewBox="0 0 58 58" aria-hidden="true">
        <circle cx="29" cy="29" r="28" fill="#6d6e71" stroke="#fff" stroke-width="1"/>
        <path d="M14 16h7l2 2h8v9H14z" fill="#fff"/>
        <path d="M28 31h7l2 2h8v9H28z" fill="#fff"/>
        <path d="M35 20h5v6" fill="none" stroke="#fff" stroke-width="2"/>
        <path d="M37 25l3 3 3-3" fill="none" stroke="#fff" stroke-width="2"/>
        <path d="M22 42h-5v-6" fill="none" stroke="#fff" stroke-width="2"/>
        <path d="M14 37l3-3 3 3" fill="none" stroke="#fff" stroke-width="2"/>
      </svg>
      <h3>Data Exchange:</h3>
      <p>When missed revenue is found, a simple data exchange will be recommended. Through the exchange, PLUM will arrange to connect your claims data into the PLUM work flow.</p>
    </div>

    <div class="step" style="top:280px">
      <svg class="step-icon" style="top:-4px" viewBox="0 0 58 58" aria-hidden="true">
        <circle cx="29" cy="29" r="28" fill="#6d6e71" stroke="#fff" stroke-width="1"/>
        <path d="M24 15h10l-3 5h-4z" fill="#fff"/>
        <path d="M27 21h4c8 4 11 10 11 15 0 5-4 7-13 7s-13-2-13-7c0-5 3-11 11-15z" fill="#fff"/>
        <circle cx="29" cy="33" r="6" fill="none" stroke="#6d6e71" stroke-width="1.6"/>
        <text x="29" y="37" text-anchor="middle" font-family="Open Sans, sans-serif" font-size="10" font-weight="700" fill="#6d6e71">$</text>
      </svg>
      <h3>Collections:</h3>
      <p>PLUM disperses underpaid claims to our medical billers for prompt recovery.</p>
    </div>
  </section>

  <footer class="cta">
    <span class="cta-label">GET PLUM TODAY!</span>
    <svg class="cta-icon" viewBox="0 0 38 38" aria-hidden="true">
      <circle cx="19" cy="19" r="16.5" fill="none" stroke="#fff" stroke-width="2.5"/>
      <path d="M13 11c1-1 2-1 3 0l2 3c.6 1 .3 2-.5 2.6l-1 .8c1 2.3 2.8 4.2 5 5.2l.9-1c.7-.8 1.7-1 2.6-.4l3 2c1 .7 1 1.8.2 2.7l-1.2 1.3c-1.2 1.2-3 1.4-4.6.6-4.5-2.2-8-5.8-10-10.4-.7-1.6-.4-3.3.8-4.5z" fill="#fff"/>
    </svg>
    <span class="cta-phone">1-800-555-0142</span>
  </footer>
</main>
</body>
</html>
```